Business card design needed

play house and learning centre for toddlers and pre-schoolers, before and after school care for primary school aged children

focus on fun, bright and natural outdoor setting, art and creative play and activities
emphasis on durability, comfort and safety in facilities - child height and accessible to encourage independence, skills development and healthy interaction with others
Updates

Hi All

I will now be looking at the one-sided designs only after careful consideration.  My friends whom I have consulted on the designs have pointed out the practicalities of having all information on front page and having uncluttered blank space to write appointments or their own notes about their contact on the business card.

Please bear this in mind when submitting designs and a big  thank you for those who have taken the time to submit both two and one-sided designs.

Please note the organisation of the information on the card (without necessarily using the labels I had placed here or the font sizes which are not my settings, or the indents) as follows:

Business name: Maple Nook Tots

Tag: Family Day Care & OSH Care

Name: Lorna Beltran Okafor

Position Title: Registered Family Day Care Educator

ABN: 57 318 902 641

Street Address: 19 Pellow Avenue Fernhill NSW 2417

Postal Address: PO Box 71 Ashgrove NSW 2418

Mobile: 0491 736 524

Email: lorna.b.okafor@mailbay.example

Please note three changes with the information: the position title, street address and mobile phone.

Thanks.

Reason: Hi all. Just giving a little more time for final revisions and I will be opening up remaining designs to a voting poll. We're almost there!

Hi all

Tonight is the absolute deadline for my business card design project so please submit your final entries as I hope to make a decision by 8pm.  

Thanks to all those who have made submissions.  I really appreciate your ideas, creativity and efforts.  Your designs have reflected back to me the impressions that you have made from what I am trying to communicate with my business, as well as told me how well I have presented the brief.  As professionals in your field, I am sure you are aware of the importance of first impressions with business cards and I am grateful to have had this opportunity to work in this way and try out this method for the first time to achieve a great design with your participation.

Target Market(s)

parents (aged 25 - 45) of young children either high earning professionals or single income families, primary schools, toddlers and pre-schoolers

Industry/Entity Type

School

Contact Information for Business Card

Maple Nook Tots
Family Day Care & OSH Care
Lorna Beltran Okafor
Registered Early Childhood Carer & Educator
ABN 57 318 902 641

19 Pellow Avenue New Lambton NSW
PO Box 71 Ashgrove NSW 2418
M: 0491 736 524
E: lorna.b.okafor@mailbay.example

```html
<!DOCTYPE html>
<html lang="en">
<head>
<meta charset="utf-8">
<title>Maple Nook Tots – Business Card</title>
<link rel="stylesheet" href="https://fonts.googleapis.com/css2?family=Sniglet:wght@400;800&display=swap">
<style>
  :root {
    --backdrop: #e4e4e4;
    --card-base: #4a4043;
    --text-light: #ffffff;
    --text-accent: #ffe11a;
    --hill-green: #86b71c;
    --hill-orange: #dd7d0c;
    --figure-green: #7fb01a;
    --figure-orange: #e08a14;
    --rule: #ffffff;
  }
  * { margin: 0; padding: 0; box-sizing: border-box; }
  html, body {
    width: 1200px;
    height: 807px;
    overflow: hidden;
    background: var(--backdrop);
    font-family: "Sniglet", "Comic Sans MS", sans-serif;
  }
  .canvas {
    position: relative;
    width: 1200px;
    height: 807px;
  }
  .business-card {
    position: absolute;
    left: 180px;
    top: 163px;
    width: 840px;
    height: 480px;
    background: var(--card-base);
    overflow: hidden;
    box-shadow: 0 6px 18px rgba(0,0,0,0.25);
  }
  .card-scenery {
    position: absolute;
    inset: 0;
    width: 840px;
    height: 480px;
  }
  .brand-name {
    position: absolute;
    top: 20px;
    left: 0;
    width: 840px;
    text-align: center;
    font-weight: 800;
    font-size: 42px;
    line-height: 1;
    color: var(--text-light);
  }
  .brand-tagline {
    position: absolute;
    top: 66px;
    right: 160px;
    font-size: 18px;
    font-weight: 800;
    color: var(--text-accent);
  }
  .header-rule {
    position: absolute;
    top: 96px;
    left: 22px;
    right: 22px;
    height: 2px;
    background: var(--rule);
  }
  .contact-block {
    position: absolute;
    top: 114px;
    left: 0;
    width: 840px;
    text-align: center;
  }
  .person-name {
    font-size: 32px;
    font-weight: 800;
    color: var(--text-accent);
    line-height: 1.1;
  }
  .person-role {
    margin-top: 6px;
    font-size: 17px;
    font-weight: 800;
    color: var(--text-light);
  }
  .business-abn {
    margin-top: 6px;
    font-size: 15px;
    font-weight: 400;
    color: var(--text-light);
  }
  .mobile-number {
    margin-top: 4px;
    font-size: 30px;
    font-weight: 800;
    color: var(--text-accent);
  }
  .email-address {
    position: absolute;
    left: 22px;
    bottom: 58px;
    font-size: 18px;
    font-weight: 400;
    color: var(--text-light);
  }
  .postal-details {
    position: absolute;
    right: 26px;
    bottom: 20px;
    font-size: 15px;
    font-weight: 800;
    font-style: normal;
    color: var(--text-accent);
    text-align: left;
    line-height: 1.3;
  }
</style>
</head>
<body>
<main class="canvas">
  <section class="business-card">
    <svg class="card-scenery" viewBox="0 0 840 480">
      <rect class="figure-slot" role="img" aria-label="Silhouette of a child walking" x="38" y="205" width="64" height="115" rx="24" fill="var(--figure-green)"/>
      <rect class="figure-slot" role="img" aria-label="Silhouette of a child doing a cartwheel" x="222" y="210" width="82" height="105" rx="24" fill="var(--figure-green)"/>
      <rect class="figure-slot" role="img" aria-label="Silhouette of a child jumping with arms raised" x="548" y="275" width="80" height="125" rx="24" fill="var(--figure-orange)"/>
      <rect class="figure-slot" role="img" aria-label="Silhouette of a child carrying a bag" x="732" y="258" width="54" height="114" rx="22" fill="var(--figure-orange)"/>
      <path class="hill-green" d="M0 330 C 150 300, 360 305, 520 400 L 520 480 L 0 480 Z" fill="var(--hill-green)"/>
      <path class="hill-orange" d="M360 480 C 440 410, 620 375, 840 365 L 840 480 Z" fill="var(--hill-orange)"/>
    </svg>

    <h1 class="brand-name">Maple Nook Tots</h1>
    <p class="brand-tagline">Family Day Care &amp; OSH Care</p>
    <div class="header-rule"></div>

    <div class="contact-block">
      <p class="person-name">Lorna Beltran Okafor</p>
      <p class="person-role">Registered Family Day Care Educator</p>
      <p class="business-abn">ABN: 57 318 902 641</p>
      <p class="mobile-number">0491 736 524</p>
    </div>

    <p class="email-address">lorna.b.okafor@mailbay.example</p>
    <address class="postal-details">
      19 Pellow Avenue Fernhill NSW 2417<br>
      PO Box 71 Ashgrove NSW 2418
    </address>
  </section>
</main>
</body>
</html>
```